Business Cards for Lean-Right-In

I need a business card that uses elements of my color pallet and book along with my company name and logo. The primary thing I'd like to have stand out is the word Lean-Right-In (i'd like to see this word in the orange from my pallet)
On the back of the card I want it to say Stop being Accountable, Be Lean-Right-In

Contact Information for Business Card

Q-Tier Fireside logo, Lean-Right-In, email - mpr@qtierfireside.example, phone 555-204-8817, Portland | Halifax

Requirements
Nice to have
• colors from my color pallet

```html
<!DOCTYPE html>
<html lang="en">
<head>
<meta charset="utf-8">
<title>Lean-Right-In Business Card</title>
<link href="https://fonts.googleapis.com/css2?family=Montserrat:wght@500;700;800&family=Oswald:wght@700&display=swap" rel="stylesheet">
<style>
  :root {
    --bg: #3a3b3e;
    --card: #f1f1f2;
    --navy: #262a63;
    --band: #2b3585;
    --band-deep: #1f2566;
    --orange: #e8612c;
    --logo-blue: #1e76c0;
    --ink: #2a2a33;
  }
  * { box-sizing: border-box; margin: 0; padding: 0; }
  html, body { width: 1200px; height: 912px; overflow: hidden; }
  body {
    background: var(--bg);
    font-family: "Montserrat", Arial, sans-serif;
    position: relative;
  }
  .card {
    position: absolute;
    width: 620px;
    height: 354px;
    background: var(--card);
    border-bottom: 3px solid var(--orange);
    overflow: hidden;
  }
  /* Slogan side */
  .card--slogan { left: 110px; top: 64px; }
  .slogan {
    position: absolute; inset: 0;
    display: flex; flex-direction: column; align-items: center; justify-content: center;
    text-align: center; font-weight: 800; color: var(--navy); line-height: 1;
  }
  .slogan__stop { font-size: 104px; letter-spacing: 2px; }
  .slogan__line { font-size: 38px; margin-top: 10px; letter-spacing: 1px; }
  .slogan__accent { color: var(--orange); }

  /* Contact side */
  .card--contact { left: 470px; top: 486px; }
  .title-band {
    position: absolute; left: 0; top: 0; width: 100%; height: 128px;
    background: linear-gradient(90deg, var(--band-deep), var(--band));
    border-radius: 0 0 40px 40px;
    display: flex; align-items: center; justify-content: center;
  }
  .title-band__word {
    font-family: "Oswald", "Arial Narrow", sans-serif;
    font-weight: 700; font-size: 92px; color: var(--orange);
    letter-spacing: 1px; line-height: 1;
  }
  .holder {
    position: absolute; left: 44px; top: 166px;
  }
  .holder__name { font-weight: 800; font-size: 28px; color: var(--navy); letter-spacing: 1px; }
  .contact-list { list-style: none; margin-top: 22px; }
  .contact-list li {
    display: flex; align-items: center; gap: 10px;
    font-size: 17px; font-weight: 500; color: var(--ink); margin-bottom: 8px;
  }
  .contact-list svg { width: 16px; height: 16px; fill: var(--orange); flex: none; }
  .brand {
    position: absolute; right: 34px; top: 178px; width: 200px; text-align: center;
  }
  .brand__dot {
    width: 54px; height: 54px; border-radius: 50%; background: var(--logo-blue);
    margin: 0 auto 12px;
  }
  .brand__name { font-weight: 500; font-size: 24px; color: var(--logo-blue); line-height: 1.1; }
  .brand__tagline { font-weight: 500; font-size: 11px; color: var(--logo-blue); margin-top: 6px; }
</style>
</head>
<body>

  <section class="card card--slogan">
    <div class="slogan">
      <span class="slogan__stop">STOP</span>
      <span class="slogan__line">BEING ACCOUNTABLE</span>
      <span class="slogan__line">BE <span class="slogan__accent">LEAN-RIGHT-IN</span></span>
    </div>
  </section>

  <section class="card card--contact">
    <div class="title-band">
      <span class="title-band__word">LEAN-RIGHT-IN</span>
    </div>

    <div class="holder">
      <p class="holder__name">MARA PELLERIN</p>
      <ul class="contact-list">
        <li>
          <svg viewBox="0 0 16 16" aria-hidden="true"><path d="M8 0a5.5 5.5 0 0 0-5.5 5.5C2.5 10 8 16 8 16s5.5-6 5.5-10.5A5.5 5.5 0 0 0 8 0zm0 8a2.5 2.5 0 1 1 0-5 2.5 2.5 0 0 1 0 5z"/></svg>
          Portland | Halifax
        </li>
        <li>
          <svg viewBox="0 0 16 16" aria-hidden="true"><path d="M3.6 1 6 3.6 4.6 5.6a9 9 0 0 0 5.8 5.8L12.4 10 15 12.4l-1.6 2.4C7.6 15 1 8.4 1.2 2.6z"/></svg>
          555-204-8817
        </li>
        <li>
          <svg viewBox="0 0 16 16" aria-hidden="true"><path d="M1 3h14v1.2L8 9 1 4.2zm0 2.8 7 4.8 7-4.8V13H1z"/></svg>
          mpr@qtierfireside.example
        </li>
        <li>
          <svg viewBox="0 0 16 16" aria-hidden="true"><path d="M8 1a7 7 0 1 0 0 14A7 7 0 0 0 8 1zm5.4 6.3h-2.5a11 11 0 0 0-1-4.3 5.6 5.6 0 0 1 3.5 4.3zM8 2.6c.7.9 1.3 2.6 1.5 4.7h-3C6.7 5.2 7.3 3.5 8 2.6zM6.1 3a11 11 0 0 0-1 4.3H2.6A5.6 5.6 0 0 1 6.1 3zM2.6 8.7h2.5a11 11 0 0 0 1 4.3 5.6 5.6 0 0 1-3.5-4.3zM8 13.4c-.7-.9-1.3-2.6-1.5-4.7h3c-.2 2.1-.8 3.8-1.5 4.7zm1.9-.4a11 11 0 0 0 1-4.3h2.5a5.6 5.6 0 0 1-3.5 4.3z"/></svg>
          www.qtierfireside.example
        </li>
      </ul>
    </div>

    <div class="brand">
      <div class="brand__dot"></div>
      <p class="brand__name">Q-Tier Fireside</p>
      <p class="brand__tagline">Every Venture Needs Allies!</p>
    </div>
  </section>

</body>
</html>
```